Looking for a modern website banner design

Bramblecrest Coaching Partners looking for the development of the main banner of the website. The project description and photos are included in the upload files.

```html
<!DOCTYPE html>
<html lang="en">
<head>
<meta charset="utf-8">
<title>Bramblecrest Coaching Partners – Athlete Testimonial Banner</title>
<link rel="stylesheet" href="https://fonts.googleapis.com/css2?family=Fira+Sans:wght@300;500;700&display=swap">
<style>
  :root {
    --brand-blue: #1175bf;
    --slate-gray: #666666;
    --white: #ffffff;
    --quote-mark: #7fb2e0;
    --caption-blue: #93c4ee;
    --photo-navy: #1d2940;
    --photo-red: #c8242f;
    --photo-wood: #8a6a4a;
  }
  html, body {
    margin: 0;
    padding: 0;
    overflow: hidden;
    background: var(--white);
  }
  .banner {
    position: relative;
    width: 1200px;
    height: 562px;
    overflow: hidden;
    background: var(--brand-blue);
    font-family: "Fira Sans", Arial, sans-serif;
  }
  .banner__corner {
    position: absolute;
    inset: 0;
  }
  .testimonial {
    position: absolute;
    left: 137px;
    top: 100px;
    margin: 0;
    color: var(--white);
  }
  .testimonial__mark {
    position: absolute;
    width: 52px;
    height: 32px;
  }
  .testimonial__mark--open {
    left: -57px;
    top: -12px;
  }
  .testimonial__text {
    margin: 0;
    font-weight: 700;
    font-size: 22.5px;
    line-height: 33.3px;
    letter-spacing: -0.1px;
    white-space: nowrap;
  }
  .testimonial__mark--close {
    position: relative;
    display: inline-block;
    vertical-align: -9px;
    margin-left: 8px;
  }
  .testimonial__rule {
    width: 36px;
    height: 2px;
    background: var(--white);
    margin: 34px 0 29px;
    border: 0;
  }
  .athlete__name {
    margin: 0;
    font-weight: 500;
    font-size: 22.5px;
    line-height: 28px;
  }
  .athlete__team {
    margin: 4px 0 0;
    font-weight: 300;
    font-size: 18px;
    line-height: 27px;
    color: var(--caption-blue);
  }
  .portrait {
    position: absolute;
    left: 680px;
    top: 69px;
    width: 434px;
    height: 434px;
    border-radius: 50%;
    background: var(--white);
    box-shadow: 0 6px 22px rgba(0, 0, 0, 0.28);
  }
  .portrait__photo {
    position: absolute;
    inset: 15px;
    border-radius: 50%;
    background:
      radial-gradient(circle at 78% 22%, rgba(200, 36, 47, 0.85) 0 22%, transparent 42%),
      radial-gradient(circle at 42% 78%, var(--photo-navy) 0 26%, transparent 52%),
      linear-gradient(160deg, var(--photo-wood) 0%, #3a3430 45%, var(--photo-navy) 100%);
  }
</style>
</head>
<body>
  <section class="banner">
    <svg class="banner__corner" width="1200" height="562" viewBox="0 0 1200 562" aria-hidden="true">
      <polygon points="1169,0 1200,0 1200,562 606,562" fill="var(--slate-gray)"/>
    </svg>

    <blockquote class="testimonial">
      <svg class="testimonial__mark testimonial__mark--open" viewBox="0 0 52 32" aria-hidden="true">
        <path d="M12 8 C6 8 0 13 0 20 a12 12 0 1 0 12 -12 Z M20 0 C14 2 8 5 5 11 L12 12 C13 7 17 4 21 3 Z" fill="var(--quote-mark)"/>
        <path d="M39 8 C33 8 27 13 27 20 a12 12 0 1 0 12 -12 Z M47 0 C41 2 35 5 32 11 L39 12 C40 7 44 4 48 3 Z" fill="var(--quote-mark)"/>
      </svg>
      <p class="testimonial__text">Bramblecrest has provided support that has<br>allowed me to develop as a person and<br>an athlete.&nbsp; The P.A.C.E.™ process allowed<br>me to stay focused on attainable goals each<br>season and progress from Junior to College<br>and now Professional Hockey.<svg class="testimonial__mark testimonial__mark--close" viewBox="0 0 52 32" aria-hidden="true">
        <path d="M13 0 a12 12 0 1 1 0 24 C10 26 7 30 2 32 L4 28 C7 26 9 24 9 23 A12 12 0 0 1 13 0 Z" fill="var(--quote-mark)"/>
        <path d="M40 0 a12 12 0 1 1 0 24 C37 26 34 30 29 32 L31 28 C34 26 36 24 36 23 A12 12 0 0 1 40 0 Z" fill="var(--quote-mark)"/>
      </svg></p>
      <hr class="testimonial__rule">
      <footer class="athlete">
        <p class="athlete__name">Marcus Delorme</p>
        <p class="athlete__team">Riverton Gales<br>Eastern Seaboard Hockey League</p>
      </footer>
    </blockquote>

    <figure class="portrait" style="margin:0">
      <div class="portrait__photo" role="img" aria-label="Photo of a smiling hockey player in a navy and red team jersey walking out of the tunnel while young fans in red jerseys reach out for high-fives"></div>
    </figure>
  </section>
</body>
</html>
```